Redesign of existing business card

I would like the "signage" attachment converted into a business card. This needs to be double sided aswell, keeping the phone number and names on the front, and the email + website on the back.

Second attachment is the current business card design.

Larger font for contact details is required.

Must keep to original color themes (electric blue, silver/grey etc)

Back of the card to have blue background with white writing.

Industry/Entity Type

Business

Contact Information for Business Card

Refer to existing design from attachments

Requirements
Must have
• Refer to existing design from attachments
Nice to have

```html
<!DOCTYPE html>
<html lang="en">
<head>
<meta charset="utf-8">
<title>Voltra Electro Services – Business Card</title>
<link href="https://fonts.googleapis.com/css2?family=Arimo:wght@400;700&display=swap" rel="stylesheet">
<style>
  :root{
    --electric-blue:#2537a6;
    --blue-deep:#1d2d8f;
    --silver:#c9cacc;
    --silver-light:#e4e5e6;
    --charcoal:#2a2a2c;
    --paper:#f4f4f2;
    --backdrop:#d9d9d9;
    --white:#ffffff;
  }
  *{box-sizing:border-box;margin:0;padding:0}
  html,body{width:1200px;height:1000px;overflow:hidden}
  body{background:var(--backdrop);font-family:"Arimo",Arial,sans-serif;position:relative}

  .card{position:absolute;left:330px;width:540px;height:330px;overflow:hidden;
        box-shadow:0 6px 18px rgba(0,0,0,.18)}
  .card--front{top:110px;background:var(--paper)}
  .card--back{top:560px;background:var(--electric-blue)}

  /* front */
  .accent{position:absolute;left:0;top:0;width:540px;height:330px}
  .brand{position:absolute;left:34px;top:30px;color:var(--charcoal);font-weight:700;line-height:1}
  .brand__name{font-size:64px;letter-spacing:2px}
  .brand__tag{font-size:23px;letter-spacing:3px;margin-top:6px;color:var(--electric-blue)}

  .name-bar,.phone-bar{position:absolute;left:0;width:420px;white-space:nowrap;
            color:var(--white);padding-left:92px}
  .name-bar{top:160px;height:38px;background:var(--charcoal);font-size:24px;line-height:38px}
  .phone-bar{top:198px;height:56px;background:var(--electric-blue);
             font-size:38px;font-weight:700;line-height:56px;letter-spacing:1px}
  .phone-icon{position:absolute;left:34px;top:166px;width:46px;height:82px}

  /* back */
  .contact{position:absolute;left:120px;top:70px;list-style:none;color:var(--white);font-size:24px}
  .contact__item{display:flex;align-items:center;gap:14px;height:40px;white-space:nowrap}
  .contact__icon{width:26px;height:26px;flex:none}
  .licence-strip{position:absolute;left:0;top:0;width:540px;height:330px}
  .licence{position:absolute;left:22px;bottom:16px;color:var(--electric-blue);font-weight:700;
           font-size:20px;letter-spacing:2px;white-space:nowrap}
</style>
</head>
<body>

<section class="card card--front" aria-label="Business card front">
  <svg class="accent" viewBox="0 0 540 330" aria-hidden="true">
    <polygon points="540,200 520,200 380,320 400,320" fill="var(--silver-light)"/>
    <polygon points="540,230 420,330 540,330" fill="var(--silver)"/>
    <polygon points="540,270 470,330 540,330" fill="var(--electric-blue)"/>
  </svg>

  <div class="brand">
    <div class="brand__name">VOLTRA</div>
    <div class="brand__tag">ELECTRO SERVICES</div>
  </div>

  <div class="name-bar">Daniel Reeve</div>
  <div class="phone-bar">0400 555 123</div>
  <svg class="phone-icon" viewBox="0 0 46 82" aria-label="Mobile phone">
    <rect x="3" y="3" width="40" height="76" rx="7" fill="var(--white)" stroke="var(--charcoal)" stroke-width="4"/>
    <rect x="10" y="14" width="26" height="44" rx="2" fill="none" stroke="var(--charcoal)" stroke-width="3"/>
    <circle cx="23" cy="68" r="4" fill="var(--charcoal)"/>
  </svg>
</section>

<section class="card card--back" aria-label="Business card back">
  <ul class="contact">
    <li class="contact__item">
      <svg class="contact__icon" viewBox="0 0 26 26" aria-hidden="true">
        <circle cx="13" cy="13" r="12" fill="none" stroke="var(--white)" stroke-width="2"/>
        <rect x="6.5" y="8.5" width="13" height="9" fill="none" stroke="var(--white)" stroke-width="1.6"/>
        <polyline points="6.5,8.5 13,13.5 19.5,8.5" fill="none" stroke="var(--white)" stroke-width="1.6"/>
      </svg>
      <span>dan@voltraelectro.com</span>
    </li>
    <li class="contact__item">
      <svg class="contact__icon" viewBox="0 0 26 26" aria-hidden="true">
        <circle cx="13" cy="13" r="11" fill="none" stroke="var(--white)" stroke-width="2"/>
        <ellipse cx="13" cy="13" rx="5" ry="11" fill="none" stroke="var(--white)" stroke-width="1.5"/>
        <line x1="2" y1="13" x2="24" y2="13" stroke="var(--white)" stroke-width="1.5"/>
        <line x1="4" y1="7.5" x2="22" y2="7.5" stroke="var(--white)" stroke-width="1.2"/>
        <line x1="4" y1="18.5" x2="22" y2="18.5" stroke="var(--white)" stroke-width="1.2"/>
      </svg>
      <span>www.voltraelectro.com.au</span>
    </li>
  </ul>

  <svg class="licence-strip" viewBox="0 0 540 330" aria-hidden="true">
    <polygon points="0,278 150,278 120,330 0,330" fill="var(--paper)"/>
  </svg>
  <div class="licence">EC24810</div>
</section>

</body>
</html>
```